Banner Ad Design Project

We are a SEO company and need a banner design for our new service, the highlights being:

- Pay Per Performance SEO service
- Guaranteed Frobly page 1 ranking
- Only $197 per month (+ performance bonus)

Can be all on one static banner or made into an animated GIF - designers choice...

Site URL (not up yet) will be RankLoft.com (by Velbrin) - this is a spinoff site of our existing business, Velbrin LLC - logo attached and should be included on the banner.

Industry/Entity Type

Business

Requirements
Must have
• Banner delivered in multiple sizes:
- 200 x 200
- 250 x 250
- 300 x 250
- 336 x 280
- 468 x 60
- 728 x 90
- 120 x 600
- 160 x 600

```html
<!DOCTYPE html>
<html lang="en">
<head>
<meta charset="utf-8">
<title>Velbrin SEO Banner Set</title>
<link rel="stylesheet" href="https://fonts.googleapis.com/css2?family=Roboto+Condensed:wght@400;700&display=swap">
<style>
  :root {
    --backdrop: #5a2d17;
    --blue-light: #2f6fd0;
    --blue-mid: #1d4fa8;
    --blue-dark: #0d2c73;
    --logo-blue: #1f3f96;
    --logo-green: #8cc63f;
    --price-top: #fff3a0;
    --price-bottom: #f2b705;
    --btn-top: #b8ea5a;
    --btn-bottom: #5ea31c;
    --btn-text: #14320a;
    --white: #ffffff;
    --photo-a: #d9cfc6;
    --photo-b: #3a3a44;
  }
  * { box-sizing: border-box; margin: 0; padding: 0; }
  html, body { width: 1200px; height: 836px; overflow: hidden; background: var(--backdrop); }
  body { font-family: "Roboto Condensed", "Arial Narrow", sans-serif; color: var(--white); }

  .stage { position: relative; width: 1042px; height: 726px; transform: scale(1.1516); transform-origin: 0 0; }

  .banner {
    position: absolute; overflow: hidden;
    background: linear-gradient(180deg, var(--blue-light) 0%, var(--blue-mid) 45%, var(--blue-dark) 100%);
    box-shadow: 0 3px 8px rgba(0,0,0,.45);
  }
  .white-band { position: absolute; background: var(--white); }
  .photo {
    position: absolute;
    background: linear-gradient(160deg, var(--photo-a) 0%, #b9a89a 45%, var(--photo-b) 100%);
  }
  .brand { position: absolute; display: flex; align-items: center; gap: 6px; }
  .brand-dot { border-radius: 50%; background: var(--logo-green); flex: none; }
  .brand-name { color: var(--logo-blue); font-weight: 700; line-height: 1; }

  .point { position: absolute; display: flex; align-items: flex-start; line-height: 1.1; }
  .tick { flex: none; fill: none; stroke: var(--white); stroke-width: 3; stroke-linecap: round; stroke-linejoin: round; }

  .offer { position: absolute; text-align: center; line-height: 1; }
  .offer-only { display: block; }
  .offer-price {
    display: block; font-weight: 700;
    background: linear-gradient(180deg, var(--price-top), var(--price-bottom));
    -webkit-background-clip: text; background-clip: text; color: transparent;
  }
  .offer-term, .offer-bonus { display: block; }

  .cta {
    position: absolute; display: flex; align-items: center; justify-content: center;
    background: linear-gradient(180deg, var(--btn-top), var(--btn-bottom));
    border: 2px solid #e9f7d6; border-radius: 5px; color: var(--btn-text); font-weight: 700;
  }

  /* 160 x 600 skyscraper */
  .sky { left: 75px; top: 68px; width: 160px; height: 600px; }
  .sky .white-band { left: 0; top: 0; width: 160px; height: 143px; }
  .sky .photo { left: 0; top: 0; width: 72px; height: 143px; }
  .sky .brand { left: 70px; top: 12px; flex-direction: column; gap: 6px; }
  .sky .brand-dot { width: 62px; height: 62px; }
  .sky .brand-name { font-size: 28px; }
  .sky .point { left: 5px; font-size: 23px; }
  .sky .point .tick { width: 24px; height: 24px; margin: 8px 6px 0 0; }
  .sky .p1 { top: 158px; }
  .sky .p1 .lead { font-size: 36px; display: block; }
  .sky .p2 { top: 270px; }
  .sky .p2 .big { font-size: 30px; }
  .sky .offer { left: 0; width: 160px; top: 388px; }
  .sky .offer-only { font-size: 44px; }
  .sky .offer-price { font-size: 58px; margin-top: 4px; }
  .sky .offer-term { font-size: 19px; margin-top: 4px; }
  .sky .offer-bonus { font-size: 15px; margin-top: 4px; }
  .sky .cta { left: 9px; top: 557px; width: 141px; height: 33px; font-size: 19px; }

  /* 336 x 280 */
  .rect-lg { left: 294px; top: 68px; width: 336px; height: 280px; }
  .rect-lg .white-band { left: 0; top: 0; width: 336px; height: 70px; }
  .rect-lg .photo { left: 0; top: 0; width: 160px; height: 280px; border-radius: 0 0 60px 0; }
  .rect-lg .brand { left: 100px; top: 6px; }
  .rect-lg .brand-dot { width: 58px; height: 58px; }
  .rect-lg .brand-name { font-size: 40px; }
  .rect-lg .point { left: 82px; font-size: 16px; }
  .rect-lg .point .tick { width: 20px; height: 20px; margin-right: 6px; }
  .rect-lg .p1 { top: 90px; }
  .rect-lg .p2 { top: 127px; }
  .rect-lg .offer { left: 150px; width: 170px; top: 160px; }
  .rect-lg .offer-only { display: inline; font-size: 30px; }
  .rect-lg .offer-price { display: inline; font-size: 50px; }
  .rect-lg .offer-term, .rect-lg .offer-bonus { font-size: 11px; margin-top: 2px; }
  .rect-lg .cta { left: 190px; top: 246px; width: 107px; height: 24px; font-size: 14px; }

  /* 300 x 250 */
  .rect-md { left: 665px; top: 68px; width: 300px; height: 250px; }
  .rect-md .white-band { left: 0; top: 0; width: 300px; height: 62px; }
  .rect-md .photo { left: 0; top: 0; width: 148px; height: 250px; border-radius: 0 0 55px 0; }
  .rect-md .brand { left: 92px; top: 5px; }
  .rect-md .brand-dot { width: 52px; height: 52px; }
  .rect-md .brand-name { font-size: 36px; }
  .rect-md .point { left: 74px; font-size: 14px; }
  .rect-md .point .tick { width: 18px; height: 18px; margin-right: 5px; }
  .rect-md .p1 { top: 82px; }
  .rect-md .p2 { top: 114px; }
  .rect-md .offer { left: 130px; width: 160px; top: 143px; }
  .rect-md .offer-only { display: inline; font-size: 27px; }
  .rect-md .offer-price { display: inline; font-size: 44px; }
  .rect-md .offer-term, .rect-md .offer-bonus { font-size: 10px; margin-top: 2px; }
  .rect-md .cta { left: 169px; top: 218px; width: 96px; height: 22px; font-size: 13px; }

  /* 468 x 60 */
  .lb-sm { left: 396px; top: 447px; width: 468px; height: 58px; }
  .lb-sm .white-band { left: 0; top: 0; width: 114px; height: 58px; }
  .lb-sm .photo { left: 0; top: 0; width: 40px; height: 58px; }
  .lb-sm .brand { left: 44px; top: 4px; flex-direction: column; gap: 2px; }
  .lb-sm .brand-dot { width: 28px; height: 28px; }
  .lb-sm .brand-name { font-size: 19px; }
  .lb-sm .point { left: 124px; font-size: 11px; }
  .lb-sm .point .tick { width: 13px; height: 13px; margin-right: 4px; }
  .lb-sm .p1 { top: 7px; }
  .lb-sm .p2 { top: 34px; }
  .lb-sm .offer { left: 312px; width: 60px; top: 5px; }
  .lb-sm .offer-only { font-size: 15px; }
  .lb-sm .offer-price { font-size: 22px; }
  .lb-sm .offer-term { font-size: 7px; }
  .lb-sm .offer-bonus { position: absolute; left: 377px; top: 11px; font-size: 8px; }
  .lb-sm .cta { left: 377px; top: 26px; width: 82px; height: 19px; font-size: 11px; }

  /* 728 x 90 */
  .lb-lg { left: 266px; top: 541px; width: 728px; height: 90px; }
  .lb-lg .white-band { left: 0; top: 0; width: 176px; height: 90px; }
  .lb-lg .photo { left: 0; top: 0; width: 62px; height: 90px; }
  .lb-lg .brand { left: 72px; top: 4px; flex-direction: column; gap: 3px; }
  .lb-lg .brand-dot { width: 46px; height: 46px; }
  .lb-lg .brand-name { font-size: 30px; }
  .lb-lg .point { left: 192px; font-size: 19px; }
  .lb-lg .point .tick { width: 22px; height: 22px; margin-right: 8px; }
  .lb-lg .p1 { top: 11px; }
  .lb-lg .p2 { top: 52px; }
  .lb-lg .offer { left: 494px; width: 80px; top: 6px; }
  .lb-lg .offer-only { font-size: 26px; }
  .lb-lg .offer-price { font-size: 36px; }
  .lb-lg .offer-term { font-size: 12px; }
  .lb-lg .offer-bonus { position: absolute; left: 588px; top: 17px; font-size: 13px; }
  .lb-lg .cta { left: 586px; top: 41px; width: 128px; height: 31px; font-size: 18px; }
</style>
</head>
<body>
<svg width="0" height="0" style="position:absolute">
  <defs>
    <symbol id="tick-mark" viewBox="0 0 24 24"><path d="M3 13 L9 19 L21 4"/></symbol>
  </defs>
</svg>

<main class="stage">

  <section class="banner sky" aria-label="160 by 600 banner">
    <div class="white-band"></div>
    <div class="photo" role="img" aria-label="Photo of a smiling businesswoman in a dark suit"></div>
    <div class="brand"><span class="brand-dot"></span><span class="brand-name">Velbrin</span></div>
    <div class="point p1"><svg class="tick"><use href="#tick-mark"/></svg><span><span class="lead">Pay Per</span>Performance SEO service</span></div>
    <div class="point p2"><svg class="tick"><use href="#tick-mark"/></svg><span>Guaranteed Frobly page <span class="big">1 ranking</span></span></div>
    <div class="offer"><span class="offer-only">Only</span><span class="offer-price">$197</span><span class="offer-term">per month</span><span class="offer-bonus">(+ performance bonus)</span></div>
    <div class="cta">Learn More!</div>
  </section>

  <section class="banner rect-lg" aria-label="336 by 280 banner">
    <div class="white-band"></div>
    <div class="photo" role="img" aria-label="Photo of a smiling businesswoman with folded arms"></div>
    <div class="brand"><span class="brand-dot"></span><span class="brand-name">Velbrin</span></div>
    <div class="point p1"><svg class="tick"><use href="#tick-mark"/></svg><span>Pay Per Performance SEO service</span></div>
    <div class="point p2"><svg class="tick"><use href="#tick-mark"/></svg><span>Guaranteed Frobly page 1 ranking</span></div>
    <div class="offer"><span class="offer-only">Only </span><span class="offer-price">$197</span><span class="offer-term">per month</span><span class="offer-bonus">(+ performance bonus)</span></div>
    <div class="cta">Learn More!</div>
  </section>

  <section class="banner rect-md" aria-label="300 by 250 banner">
    <div class="white-band"></div>
    <div class="photo" role="img" aria-label="Photo of a smiling businesswoman with folded arms"></div>
    <div class="brand"><span class="brand-dot"></span><span class="brand-name">Velbrin</span></div>
    <div class="point p1"><svg class="tick"><use href="#tick-mark"/></svg><span>Pay Per Performance SEO service</span></div>
    <div class="point p2"><svg class="tick"><use href="#tick-mark"/></svg><span>Guaranteed Frobly page 1 ranking</span></div>
    <div class="offer"><span class="offer-only">Only </span><span class="offer-price">$197</span><span class="offer-term">per month</span><span class="offer-bonus">(+ performance bonus)</span></div>
    <div class="cta">Learn More!</div>
  </section>

  <section class="banner lb-sm" aria-label="468 by 60 banner">
    <div class="white-band"></div>
    <div class="photo" role="img" aria-label="Photo of a smiling businesswoman"></div>
    <div class="brand"><span class="brand-dot"></span><span class="brand-name">Velbrin</span></div>
    <div class="point p1"><svg class="tick"><use href="#tick-mark"/></svg><span>Pay Per Performance SEO service</span></div>
    <div class="point p2"><svg class="tick"><use href="#tick-mark"/></svg><span>Guaranteed Frobly page 1 ranking</span></div>
    <div class="offer"><span class="offer-only">Only</span><span class="offer-price">$197</span><span class="offer-term">per month</span></div>
    <span class="offer-bonus">(+ performance bonus)</span>
    <div class="cta">Learn More!</div>
  </section>

  <section class="banner lb-lg" aria-label="728 by 90 banner">
    <div class="white-band"></div>
    <div class="photo" role="img" aria-label="Photo of a smiling businesswoman"></div>
    <div class="brand"><span class="brand-dot"></span><span class="brand-name">Velbrin</span></div>
    <div class="point p1"><svg class="tick"><use href="#tick-mark"/></svg><span>Pay Per Performance SEO service</span></div>
    <div class="point p2"><svg class="tick"><use href="#tick-mark"/></svg><span>Guaranteed Frobly page 1 ranking</span></div>
    <div class="offer"><span class="offer-only">Only</span><span class="offer-price">$197</span><span class="offer-term">per month</span></div>
    <span class="offer-bonus">(+ performance bonus)</span>
    <div class="cta">Learn More!</div>
  </section>

</main>
</body>
</html>
```